Greeting Cards for all Occasions

We are a large church and are sending cards all the time for different occasions. We'd like to have 5 different cards designed that fit with our brand guidelines and logo (Attached). We'd like to have designs for the following 5x7 cards. Each title should be featured on the front, and the inside should be blank, with the back should feature the contact info below. Appropriate photos from Unsplash are welcomed.

1. Happy Birthday
2. Get Well Soon
3. Praying for You
4. Happy Anniversary
5. Thank You

Contact info to include on the back:
Millbrook Chapel
4817 Tamsin Avenue, Corona, CA 92807
www.MillbrookChapel.com I 909-418-5502

```html
<!DOCTYPE html>
<html lang="en">
<head>
<meta charset="utf-8">
<title>Happy Birthday Card – Millbrook Chapel</title>
<link rel="stylesheet" href="https://fonts.googleapis.com/css2?family=Montserrat:wght@600;800&display=swap">
<style>
  :root {
    --backdrop: #b3b0aa;
    --card-white: #f6f6f4;
    --photo-light: #eeeeeb;
    --photo-gold: #c9a55a;
    --photo-gold-soft: #e2cd98;
    --photo-mist: #dce7ea;
    --photo-grey: #d9d6d0;
    --ink: #1c1c1c;
  }
  html, body {
    margin: 0;
    width: 1200px;
    height: 800px;
    overflow: hidden;
    background: var(--backdrop);
  }
  .stage {
    position: relative;
    width: 1200px;
    height: 800px;
  }
  .card-front {
    position: absolute;
    left: 400px;
    top: 120px;
    width: 400px;
    height: 560px;
    background: var(--card-white);
    overflow: hidden;
    box-shadow: 0 14px 30px rgba(0, 0, 0, 0.12);
  }
  .card-photo {
    position: absolute;
    inset: 0;
    background:
      radial-gradient(ellipse 170px 150px at 50% 56%, var(--photo-gold) 0%, var(--photo-gold-soft) 38%, var(--photo-mist) 68%, rgba(238,238,235,0) 100%),
      radial-gradient(ellipse 260px 200px at 50% 28%, var(--photo-grey) 0%, rgba(238,238,235,0) 100%),
      linear-gradient(180deg, var(--photo-light) 0%, var(--card-white) 100%);
  }
  .card-title {
    position: absolute;
    top: 84px;
    left: 0;
    right: 0;
    margin: 0;
    text-align: center;
    font-family: "Montserrat", Arial, sans-serif;
    font-weight: 800;
    font-size: 38px;
    line-height: 1.1;
    letter-spacing: 0.5px;
    color: var(--ink);
    text-transform: uppercase;
  }
  .brand-mark {
    position: absolute;
    left: 0;
    right: 0;
    bottom: 56px;
    display: flex;
    justify-content: center;
    align-items: center;
    gap: 10px;
    font-family: "Montserrat", Arial, sans-serif;
    font-weight: 600;
    font-size: 20px;
    letter-spacing: 1.5px;
    color: var(--ink);
  }
  .brand-dot {
    width: 18px;
    height: 18px;
    border-radius: 50%;
    background: var(--ink);
  }
</style>
</head>
<body>
  <main class="stage">
    <article class="card-front">
      <div class="card-photo" role="img" aria-label="Photograph of a gold and pale blue tinsel party tassel fanning upward on a white surface scattered with soft grey confetti dots"></div>
      <h1 class="card-title">Happy<br>Birthday</h1>
      <div class="brand-mark">
        <span class="brand-dot"></span>
        <span class="brand-name">Millbrook Chapel</span>
      </div>
    </article>
  </main>
</body>
</html>
```